Bluestone Nine LLC Flyer Design

Marketing Materials for Real Estate Company. This flyer will be used to promote the company throughout the Commercial Real Estate business in the United States. The team has been together for 15 years. We are the middle guys between the Tenant, Broker, and the Owner. In the case of working with a Franchisor, we will be their Plug and Play leasing arm that will assist their new Franchisee's with their site selection, lease negotiations, design and construction management.

Target Market(s)

Real Estate Owners, Franchisor's, and Brokers

Font styles to use
Serif

Colors

Designer to choose colors to be used in the design.

Requirements
Must have
• The flyer must have......
• 1. The Best Leasing Machine On The Planet
• 2. Over the past 15 years our group has completed 4,492 lease transactions resulting in leasing 17,803,114 square feet in shopping centers across the United States.
• 3. Plug and Play Leasing Specialists. We handle the details between when the broker shows up with the space and the tenant and completing the lease negotiations, legal negotiations and documentation, and construction management to Certificate of Occupancy.
• 4. For Information Call Colette Varga at 555-014-2763 or Wendy Falk at 555-017-8302.
Nice to have
• National Tenants the we have completed transactions with....
• Pellmart, Fresh Basket, Harbor Pams, Vexo, Dunn, QV Rendo, Burrasco, Pattersons, Wrap Shack, Brewhorns, Summit Workout, ShipVo, Tredwell, PKN, Halvorsons, Q&L, Ledger Union Bank, Hen Haus-O, Lotus Kitchen, Furvo, Dex-Mart, Fieldly, and Orbit Theaters

```html
<!DOCTYPE html>
<html lang="en">
<head>
<meta charset="utf-8">
<title>Bluestone Nine LLC – The Best Leasing Machine on the Planet</title>
<link href="https://fonts.googleapis.com/css2?family=Roboto+Slab:wght@300;400;600;700&display=swap" rel="stylesheet">
<style>
  :root {
    --charcoal: #3c3a3f;
    --lime: #a6ca5e;
    --lime-deep: #7fa23a;
    --white: #ffffff;
    --mist: #dcdcde;
    --slate-violet: #545478;
    --ink: #3c3a3f;
  }
  html, body {
    margin: 0;
    padding: 0;
    overflow: hidden;
    background: var(--charcoal);
  }
  .flyer {
    position: relative;
    width: 848px;
    height: 1200px;
    overflow: hidden;
    background: var(--charcoal);
    font-family: "Roboto Slab", serif;
  }
  .flyer__shapes {
    position: absolute;
    inset: 0;
    width: 848px;
    height: 1200px;
  }
  .brand-name {
    position: absolute;
    left: 63px;
    top: 70px;
    margin: 0;
    font-size: 23px;
    font-weight: 600;
    letter-spacing: 3px;
    line-height: 1;
    color: var(--lime);
  }
  .accent-dash {
    position: absolute;
    left: 63px;
    top: 187px;
    width: 40px;
    height: 4px;
    background: var(--lime);
  }
  .headline {
    position: absolute;
    left: 63px;
    top: 203px;
    width: 282px;
    margin: 0;
    line-height: 1;
  }
  .headline__lead {
    display: block;
    font-size: 21px;
    font-weight: 300;
    color: var(--white);
  }
  .headline__key {
    display: block;
    margin-top: 22px;
    font-size: 58px;
    font-weight: 700;
    line-height: 1.1;
    letter-spacing: -1px;
    color: var(--lime);
  }
  .headline__key--white { margin-top: 0; color: var(--white); }
  .headline__tail {
    display: block;
    margin-top: 16px;
    text-align: right;
    font-size: 21px;
    font-weight: 600;
    color: var(--white);
  }
  .stat {
    position: absolute;
    left: 600px;
    top: 56px;
    width: 224px;
    margin: 0;
    text-align: center;
    font-size: 24px;
    font-weight: 700;
    line-height: 1.55;
    color: var(--white);
  }
  .story {
    position: absolute;
    left: 500px;
    top: 258px;
    width: 320px;
    color: var(--ink);
  }
  .story__title {
    margin: 0 0 6px;
    font-size: 16px;
    font-weight: 700;
    line-height: 1.25;
    color: var(--lime-deep);
  }
  .story__text {
    margin: 0 0 20px;
    font-size: 12.5px;
    font-weight: 400;
    line-height: 1.5;
  }
  .tenants {
    position: absolute;
    left: 585px;
    top: 918px;
    width: 240px;
    color: var(--ink);
  }
  .tenants__title {
    margin: 0 0 4px;
    font-size: 12px;
    font-weight: 700;
    color: var(--ink);
  }
  .tenants__list {
    margin: 0;
    font-size: 10.5px;
    line-height: 1.45;
  }
  .contact {
    position: absolute;
    right: 28px;
    top: 1068px;
    width: 320px;
    text-align: right;
    color: var(--ink);
  }
  .contact__title {
    margin: 0 0 6px;
    font-size: 15px;
    font-weight: 700;
    color: var(--charcoal);
  }
  .contact__line {
    margin: 0;
    font-size: 13px;
    line-height: 1.6;
  }
  .contact__phone { font-weight: 700; color: var(--lime-deep); }
</style>
</head>
<body>
<main class="flyer">
  <svg class="flyer__shapes" viewBox="0 0 1623 2296" preserveAspectRatio="none" aria-hidden="true">
    <path fill="var(--white)" d="M1110 170 L1623 0 L1623 1725 L620 1150 Q575 1120 595 1060 Z"/>
    <polygon fill="var(--mist)" points="1020,1380 1623,1725 1623,2296 495,2296"/>
    <path fill="var(--lime)" d="M1010 0 L1623 0 L1623 222 L1290 413 Q1262 428 1243 403 Z"/>
    <polygon fill="var(--lime)" points="0,1063 620,1420 605,1446 0,1096"/>
    <polygon fill="var(--lime)" points="418,2296 690,1830 718,1846 450,2296"/>
    <path fill="var(--slate-violet)" d="M302 1030 Q318 1005 345 1020 L673 1210 Q697 1225 683 1250 L490 1582 Q475 1605 450 1590 L120 1400 Q98 1387 110 1362 Z"/>
    <path fill="var(--slate-violet)" d="M703 1270 Q720 1245 748 1258 L1155 1493 Q1180 1508 1167 1537 L930 1947 Q912 1975 885 1960 L477 1725 Q452 1710 465 1685 Z"/>
  </svg>

  <p class="brand-name">Bluestone Nine LLC</p>
  <div class="accent-dash"></div>

  <h1 class="headline">
    <span class="headline__lead">THE BEST</span>
    <span class="headline__key">LEASING</span>
    <span class="headline__key headline__key--white">MACHINE</span>
    <span class="headline__tail">ON THE PLANET</span>
  </h1>

  <p class="stat">17,803,114 Sqft<br>Leased</p>

  <section class="story">
    <h2 class="story__title">15 Years · 4,492 Lease Transactions</h2>
    <p class="story__text">Over the past 15 years our group has completed 4,492 lease transactions resulting in leasing 17,803,114 square feet in shopping centers across the United States.</p>
    <h2 class="story__title">Plug and Play Leasing Specialists</h2>
    <p class="story__text">We handle the details between when the broker shows up with the space and the tenant and completing the lease negotiations, legal negotiations and documentation, and construction management to Certificate of Occupancy.</p>
  </section>

  <section class="tenants">
    <h3 class="tenants__title">National Tenants We Have Served</h3>
    <p class="tenants__list">Pellmart, Fresh Basket, Harbor Pams, Vexo, Dunn, QV Rendo, Burrasco, Pattersons, Wrap Shack, Brewhorns, Summit Workout, ShipVo, Tredwell, PKN, Halvorsons, Q&amp;L, Ledger Union Bank, Hen Haus-O, Lotus Kitchen, Furvo, Dex-Mart, Fieldly and Orbit Theaters</p>
  </section>

  <section class="contact">
    <h3 class="contact__title">For Information Call</h3>
    <p class="contact__line">Colette Varga <span class="contact__phone">555-014-2763</span></p>
    <p class="contact__line">Wendy Falk <span class="contact__phone">555-017-8302</span></p>
  </section>
</main>
</body>
</html>
```